Corwenna Foundation is a new grant making charity set up in the UK.

Having got a logo, we now need a website to go with it. We have worked out the text which people are going to need in order to then apply for grants. But having found out what we require they will probably need to go away and think about it.
We have to be careful of what images we use. So I have uploaded some images that we like. We are also going to be adding more pages almost immediately so need to think about the images for these.
I know basic wordpress so I will be able to add new pages/make alterations in future.
Updates
The website does need to be coded in Wordpress so that I can maintain it afterwards.
Corwenna
Brief changed to provide more money and we have also provided more possible pictures. And generally more explanation.
Target Market(s)
departments in universities, other charities doing work on relief of pain, people working in health service departments
Industry/Entity Type
Health Charity
Coding
Coded - Design and coding required
Number of Pages Required
4 page
Look and feel
Each slider illustrates characteristics of the customer's brand and the style your logo design should communicate.

```html
<!DOCTYPE html>
<html lang="en">
<head>
<meta charset="utf-8">
<title>About Us – Corwenna Foundation</title>
<link href="https://fonts.googleapis.com/css2?family=Montserrat:wght@400;600;800&family=Roboto:wght@400&display=swap" rel="stylesheet">
<style>
:root{
  --brand-blue:#0a6fc0;
  --ink:#2a2a2a;
  --body-grey:#5a5a5a;
  --white:#ffffff;
  --footer-bg:#1b1b1b;
  --footer-rule:#4a4a4a;
}
*{margin:0;padding:0;box-sizing:border-box}
html,body{width:1200px;height:1129px;overflow:hidden;background:var(--white)}
.page{position:relative;width:1200px;height:1129px;font-family:"Roboto",sans-serif}

.hero{position:absolute;left:0;top:0;width:1200px;height:329px;
  background:
    linear-gradient(90deg,rgba(15,20,25,.72) 0%,rgba(15,20,25,.45) 40%,rgba(15,20,25,.15) 100%),
    linear-gradient(180deg,#3d4a33 0%,#6b6a52 35%,#9a8a74 65%,#b9ad9c 100%);}
.hero-rule{position:absolute;left:0;top:76px;width:1200px;height:1px;background:rgba(255,255,255,.45)}
.brand-panel{position:absolute;left:0;top:0;width:420px;height:77px}
.brand{position:absolute;left:183px;top:29px;display:flex;align-items:center;gap:8px;
  font-family:"Montserrat",sans-serif;font-weight:600;color:var(--ink);font-size:15px;line-height:1;white-space:nowrap}
.brand-dot{width:14px;height:14px;border-radius:50%;background:var(--brand-blue)}

.nav{position:absolute;top:29px;left:624px;display:flex;font-family:"Montserrat",sans-serif;font-weight:600;font-size:12px;color:var(--white)}
.nav a{color:inherit;text-decoration:none;margin-right:24px;letter-spacing:.3px}
.donate{position:absolute;left:921px;top:23px;width:105px;height:26px;background:var(--brand-blue);color:var(--white);
  font-family:"Montserrat",sans-serif;font-weight:600;font-size:8.5px;letter-spacing:1px;display:flex;align-items:center;justify-content:center;text-decoration:none}

.page-title{position:absolute;left:173px;top:167px;font-family:"Montserrat",sans-serif;font-weight:800;font-size:43px;color:var(--white);letter-spacing:-.5px}

.faq{position:absolute;left:173px;top:0;width:860px}
.faq h2{position:absolute;left:0;font-family:"Montserrat",sans-serif;font-weight:400;font-size:21px;color:var(--ink);white-space:nowrap;letter-spacing:.2px}
.faq p{position:absolute;left:0;width:860px;font-size:11px;line-height:15.5px;color:var(--body-grey)}

.footer{position:absolute;left:0;top:990px;width:1200px;height:139px;background:var(--footer-bg);color:var(--white)}
.footer-links{position:absolute;top:30px;left:0;width:1200px;text-align:center;font-size:11px;word-spacing:2px}
.footer-links a{color:inherit;text-decoration:none}
.social{position:absolute;top:57px;left:557px;display:flex;gap:4px}
.social span{width:26px;height:26px;border-radius:50%;background:var(--white);display:block}
.footer-rule{position:absolute;top:103px;left:173px;width:854px;height:1px;background:var(--footer-rule)}
.copyright{position:absolute;top:114px;left:0;width:1200px;text-align:center;font-family:"Montserrat",sans-serif;font-size:9.5px}
</style>
</head>
<body>
<div class="page">
  <div class="hero" role="img" aria-label="Group photo of smiling volunteers of all ages outdoors among trees"></div>
  <svg class="brand-panel" viewBox="0 0 420 77" aria-hidden="true"><polygon points="0,0 415,0 372,77 0,77" fill="#ffffff"/></svg>
  <div class="hero-rule"></div>

  <div class="brand"><span class="brand-dot"></span><span class="brand-name">Corwenna Foundation</span></div>

  <nav class="nav"><a href="#">Home</a><a href="#">About us</a><a href="#">Grants</a><a href="#">Contact Us</a></nav>
  <a class="donate" href="#">MAKE DONATION</a>

  <h1 class="page-title">About Us</h1>

  <main class="faq">
    <h2 style="top:376px">Who are the trustees of Corwenna Foundation?</h2>
    <p style="top:416px">The initial trustees are Corwenna, Hugh &amp; Oliver Tremaine.</p>
    <p style="top:447px">A fourth trustee is about to be appointed, the legal firm of Halden Marsh</p>

    <h2 style="top:486px">Who are the medical advisers to Corwenna Foundation?</h2>
    <p style="top:526px">The medical advisers are doctors or other health professionals, who individually or collectively advise the trustees on the merit of grant applications.<br>Medical advisers are initially appointed for a five year term.</p>

    <h2 style="top:587px">How much money does Corwenna Foundation have?</h2>
    <p style="top:627px">It is unclear how much money the Foundation will have in a few years time, but currently it has about a million pounds.</p>

    <h2 style="top:672px">Where has this money come from?</h2>
    <p style="top:712px">The million pounds has been inherited from Corwenna’s father, the late Sir Edmund Harcourt, who had a large stake in the Harcourt grocery business. Further significant money is going to come from the sale of the farm where the Tremaine family currently live.</p>

    <h2 style="top:773px">Why is the foundation named after Corwenna Tremaine?</h2>
    <p style="top:813px">Corwenna Tremaine suffered from extreme pain for many years after a successful operation to cure her cancer of the tongue. Although the pain is now well controlled, the family would like the unexpected receipt of such a large amount of money from the farm, to help prevent other people going through such a difficult time.</p>
  </main>

  <footer class="footer">
    <div class="footer-links"><a href="#">Home</a> &nbsp; | &nbsp;<a href="#">About</a> | &nbsp;<a href="#">Grants</a> &nbsp;| &nbsp;<a href="#">Contact</a> &nbsp;| <a href="#">Site Map</a></div>
    <div class="social" aria-label="Social media links"><span></span><span></span><span></span></div>
    <div class="footer-rule"></div>
    <div class="copyright">© Corwenna Foundation 2021. All Rights Reserved.</div>
  </footer>
</div>
</body>
</html>
```